New Website for IT Services Business

We need an uncoded web design for a new company based in Australia called "Falcon IT". We offer specialised point of sale (POS) support to the hospitality industry. We already support hundreds of cafes and restaurants. We are also about to launch and promote a range of new services with the offering of General IT Support being the most important. Other additional services to be offered are Falcon Vault Storage, reselling and supporting Corvel Shieldware and Trelmo Suite.

We have a logo design and our colour scheme is based on the logo with the addition of charcoal grey (see attached logos). We want the pages to reflect precision and efficiency with sharp characteristics. It must be professional but playful/fun elements are encouraged.

Our target audience is restaurant and cafe owners who are interested in finding high quality POS and IT support for their business.

The main call to action on the home page should be either 'Let's Meet For Coffee!' or 'Find out more (by completing a form)'. If you are unsure about what the general text should say then you can use 'Lorem Ipsum' where required.

The site must be viewable at different resolutions and on smart phones and tablets.

The website structure will be quite simple. We require:
- one impressive landing page. Visitors will quickly determine our services and that we provide a very high level of service while also offering value for money. Obviously a clear list of links (however/wherever you like) to the other pages.
- Simple pages with a similar layout for the following:
- Services - "POS & IT Support for the Hospitality Industry" being the main one. With complementary services also listed. Another call to action on this page with the option of 'Let's Meet For Coffee' or a "More information/Pricing" form to be completed by the visitor.
- Products - will be a small online storefront for a few simple products.
- About - Business background. 2x Directors with a photo and brief Bio.
- Downloads - A list of free files to download. Includes remote access client software.
- Contact Us - Mailing address, Email addresses and Support phone number.

Please feel free to ask any questions about the design. I will assist as much as possible.

Thank you for viewing. We promise to give constructive feedback to every person who submits a design. Thank you so much.

Target Market(s)

Restaurant and Cafe owners.

Industry/Entity Type

Hospitality

Requirements
Must have
• - Viewable on different resolutions and on smart phones and tablets.
- Clear call to action of EITHER 'Let's Meet For Coffee' or a "More information/Pricing" form to be completed by the visitor.

```html
<!DOCTYPE html>
<html lang="en">
<head>
<meta charset="utf-8">
<title>Falcon IT – Let's Meet For Coffee</title>
<link rel="stylesheet" href="https://fonts.googleapis.com/css2?family=Montserrat:wght@400&family=Teko:wght@400;500&display=swap">
<style>
  :root {
    --red: #ed1c2e;
    --red-deep: #b3121f;
    --black: #000000;
    --charcoal: #2b2b2b;
    --white: #ffffff;
    --display: "Teko", sans-serif;
    --body: "Montserrat", sans-serif;
  }
  * { box-sizing: border-box; margin: 0; padding: 0; }
  html, body { width: 1200px; height: 848px; overflow: hidden; background: var(--white); }
  .page {
    position: relative;
    width: 1200px;
    height: 848px;
    overflow: hidden;
    background: linear-gradient(180deg, var(--red) 0%, var(--red) 62%, var(--red-deep) 100%);
    font-family: var(--body);
    color: var(--white);
  }
  .header-band { position: absolute; inset: 0 0 auto 0; width: 1200px; height: 260px; }
  .square-pattern {
    position: absolute; left: 790px; top: 8px; width: 410px; height: 100px;
    background: linear-gradient(90deg, rgba(237,28,46,0) 0%, rgba(237,28,46,0.55) 40%, rgba(237,28,46,0.8) 100%);
  }
  .brand {
    position: absolute; left: 77px; top: 69px;
    display: flex; align-items: center; gap: 22px;
  }
  .brand-mark { width: 96px; height: 96px; border-radius: 50%; background: var(--red); }
  .brand-name {
    font-family: var(--display); font-weight: 500; font-size: 92px; line-height: 1;
    color: var(--white); padding-top: 14px; letter-spacing: 1px;
  }
  .coffee-banner { position: absolute; left: 613px; top: 142px; width: 587px; height: 69px; }
  .coffee-banner svg { position: absolute; inset: 0; }
  .coffee-icon {
    position: absolute; left: 686px; top: 152px; width: 50px; height: 50px;
    border-radius: 50%; background: var(--white);
  }
  .coffee-title {
    position: absolute; left: 754px; top: 150px;
    font-family: var(--display); font-weight: 400; font-size: 46px; line-height: 1;
    letter-spacing: 7px; white-space: nowrap; padding-top: 6px;
  }
  .contact-form { position: absolute; left: 0; top: 0; width: 1200px; height: 848px; }
  .field { position: absolute; left: 0; width: 1121px; display: flex; }
  .field label {
    width: 328px; text-align: right; font-size: 19px; line-height: 1.8;
    padding-right: 0; color: var(--white);
  }
  .field input, .field textarea {
    position: absolute; left: 349px; width: 772px; border: none;
    background: var(--white); font-family: var(--body); font-size: 18px; resize: none;
  }
  .field-name { top: 286px; } .field-email { top: 341px; } .field-business { top: 396px; }
  .field-name input, .field-email input, .field-business input { top: 0; height: 40px; }
  .field-name label, .field-email label, .field-business label { margin-top: 3px; }
  .field-description { top: 453px; }
  .field-description label { line-height: 1.85; margin-top: 4px; }
  .field-description textarea { top: 0; height: 183px; }
  .send-button {
    position: absolute; left: 869px; top: 665px; width: 252px; height: 52px;
    border: none; background: none; cursor: pointer;
  }
  .send-button svg { position: absolute; inset: 0; }
  .send-button span {
    position: absolute; left: 106px; top: 6px;
    font-family: var(--display); font-size: 46px; line-height: 1; letter-spacing: 8px; color: var(--white);
  }
  .back-home {
    position: absolute; left: 62px; top: 736px; width: 200px; height: 80px;
    text-decoration: none; color: var(--white);
  }
  .back-home-mark {
    position: absolute; left: 58px; top: 2px; width: 74px; height: 74px;
    border-radius: 50%; background: var(--black);
  }
  .back-home-label {
    position: absolute; left: 0; top: 16px;
    font-family: var(--display); font-size: 42px; line-height: 1; letter-spacing: 2px; white-space: nowrap;
  }
</style>
</head>
<body>
<main class="page">
  <svg class="header-band" viewBox="0 0 1200 260" aria-hidden="true">
    <defs>
      <radialGradient id="logoGlow" cx="300" cy="110" r="340" gradientUnits="userSpaceOnUse">
        <stop offset="0" stop-color="#3a3a3a"/>
        <stop offset="1" stop-color="#000000"/>
      </radialGradient>
    </defs>
    <path d="M0 0 H1200 V72 C1020 70 880 78 760 110 C600 160 440 245 0 232 Z" fill="url(#logoGlow)"/>
  </svg>

  <div class="square-pattern" role="img" aria-label="Scattered red square pattern"></div>

  <div class="brand">
    <span class="brand-mark"></span>
    <span class="brand-name">Falcon IT</span>
  </div>

  <div class="coffee-banner">
    <svg viewBox="0 0 587 69" aria-hidden="true"><polygon points="40,0 587,0 587,69 0,69" fill="#000"/></svg>
  </div>
  <span class="coffee-icon"></span>
  <h1 class="coffee-title">Let's Meet For Coffee</h1>

  <form class="contact-form">
    <div class="field field-name"><label for="name">Name</label><input id="name" type="text"></div>
    <div class="field field-email"><label for="email">Email Address</label><input id="email" type="email"></div>
    <div class="field field-business"><label for="business">Business Type</label><input id="business" type="text"></div>
    <div class="field field-description"><label for="description">Service Request<br>/ Description</label><textarea id="description"></textarea></div>
    <button class="send-button" type="button">
      <svg viewBox="0 0 252 52" aria-hidden="true"><polygon points="36,0 252,0 252,52 0,52" fill="#000"/></svg>
      <span>Send</span>
    </button>
  </form>

  <a class="back-home" href="#">
    <span class="back-home-mark"></span>
    <span class="back-home-label">Back to Home</span>
  </a>
</main>
</body>
</html>
```